'Wedding Business" Business Card Design

dj services for weddings and parties, uplighting, event planning, day of coordination for weddings, photography for weddings and other events.

Would like raised print and metallic also if possible. Elegant design, yet modern. This is a wedding business and should describe our goals and main services - DJ/lighting, wedding and event planning, photography. slogan "Simply Incredible, Incredibly simple" or "Your Dreams. Our Experience. The Perfect Match" Our goal is to provide multiple services to make it easier for the bride and groom almost like a one stop shop. Feel free to use the slogan or leave it out , we just want to really stand out against the competition. You can also get more info on our website www.bluelarkproductions.com - we are working to get the bluelarkct.com site pointed to our current site!

there should be 2 files attached, if they did not go through please email events@bluelarkct.com or bluelarkproductions@mailbox.test
Updates

Thank you all for your help, we have decided what we like but would like to make some changes, we need to order these asap so please let us know if you can help.

Reason: Wasn't able to pick it out in time! So Sorry but we know what we want!!

Industry/Entity Type

Business

Contact Information for Business Card

Trevor and Mallory Quenby
555-318-2746
555-207-4831
Blue Lark Productions, Events, & Photography
EMAIL:Events@BlueLarkCT.com
www.bluelarkct.com

```html
<!DOCTYPE html>
<html lang="en">
<head>
<meta charset="utf-8">
<title>Blue Lark Productions – Business Card</title>
<link rel="stylesheet" href="https://fonts.googleapis.com/css2?family=Michroma&family=Russo+One&display=swap">
<style>
  :root {
    --page-bg: #d9d6d0;
    --card-dark: #161616;
    --card-dark-edge: #2a2a2a;
    --ink-light: #eef0f5;
    --ink-soft: #c9ccd4;
    --accent-blue: #3f5bff;
    --accent-glow: #7f93ff;
    --hall-blue: #2c3a9a;
    --hall-deep: #141a52;
    --deck-red: #6a1812;
    --deck-black: #0c0c10;
    --couple-warm: #a58c80;
    --couple-dark: #3b3340;
    --banner: rgba(12, 16, 40, 0.72);
  }
  * { box-sizing: border-box; margin: 0; padding: 0; }
  html, body { width: 1200px; height: 871px; overflow: hidden; }
  body {
    background: var(--page-bg);
    position: relative;
    font-family: "Michroma", sans-serif;
  }
  .card {
    position: absolute;
    width: 540px;
    height: 309px;
    border-radius: 4px;
    overflow: hidden;
    box-shadow: 0 6px 18px rgba(0,0,0,0.25);
  }

  /* Front */
  .card-front { left: 70px; top: 110px; background: var(--hall-deep); }
  .photo { position: absolute; }
  .photo-hall {
    inset: 0;
    background: radial-gradient(ellipse at 55% 60%, #4f63d6 0%, var(--hall-blue) 35%, var(--hall-deep) 80%);
  }
  .photo-deck {
    left: 0; bottom: 0; width: 260px; height: 200px;
    background: radial-gradient(circle at 60% 65%, #c23b2a 0%, var(--deck-red) 30%, var(--deck-black) 75%);
  }
  .photo-couple {
    right: 0; top: 0; width: 210px; height: 309px;
    background: linear-gradient(160deg, var(--couple-dark) 0%, var(--couple-warm) 55%, #e6dcd4 100%);
    clip-path: polygon(18% 0, 100% 0, 100% 100%, 40% 100%);
  }
  .title-band {
    position: absolute; left: 0; top: 36px; width: 360px; height: 92px;
    background: var(--banner);
    border-top: 1px solid rgba(140,170,255,0.5);
    border-bottom: 1px solid rgba(140,170,255,0.5);
    display: flex; flex-direction: column; justify-content: center; align-items: center;
    gap: 8px;
  }
  .company-name {
    color: var(--ink-light);
    font-size: 12px;
    letter-spacing: 2.5px;
    text-transform: uppercase;
    text-align: center;
    line-height: 1.7;
  }
  .front-mark {
    color: var(--ink-light);
    font-size: 8px;
    letter-spacing: 2px;
    text-transform: uppercase;
  }

  /* Back */
  .card-back {
    left: 590px; top: 452px;
    background:
      radial-gradient(ellipse at 55% 45%, #3a3a3a 0%, var(--card-dark-edge) 40%, var(--card-dark) 100%);
  }
  .brand-mark {
    position: absolute; left: 34px; top: 70px;
    width: 110px; height: 150px;
    display: flex; align-items: center; justify-content: center;
    flex-direction: column;
    color: var(--ink-light);
    font-size: 22px;
    line-height: 1.3;
    text-align: center;
  }
  .contact {
    position: absolute; left: 168px; top: 92px; right: 26px;
    text-align: center;
  }
  .owners {
    font-family: "Russo One", sans-serif;
    color: var(--accent-blue);
    font-size: 16px;
    letter-spacing: 1.5px;
    text-transform: uppercase;
    margin-bottom: 12px;
  }
  .contact-line {
    color: var(--ink-soft);
    font-size: 10.5px;
    letter-spacing: 2px;
    text-transform: uppercase;
    line-height: 2;
  }
</style>
</head>
<body>
  <section class="card card-front" aria-label="Card front">
    <div class="photo photo-hall" role="img" aria-label="Photo of a reception hall with blue uplighting and white floral centrepieces"></div>
    <div class="photo photo-deck" role="img" aria-label="Photo of a DJ's hands on a turntable deck"></div>
    <div class="photo photo-couple" role="img" aria-label="Photo of a bride and groom embracing"></div>
    <div class="title-band">
      <p class="company-name">Blue Lark Productions<br>Events, &amp; Photography</p>
      <p class="front-mark">Blue Lark</p>
    </div>
  </section>

  <section class="card card-back" aria-label="Card back">
    <div class="brand-mark"><span>Blue</span><span>Lark</span></div>
    <div class="contact">
      <p class="owners">Trevor and Mallory Quenby</p>
      <p class="contact-line">555-318-2746</p>
      <p class="contact-line">555-207-4831</p>
      <p class="contact-line">Email:Events@BlueLarkCT.com</p>
      <p class="contact-line">www.bluelarkct.com</p>
    </div>
  </section>
</body>
</html>
```